Flyer Design for Private Car Service

Flyer should cater to Business Travelers and Executives who travel Business Class or First Class.
Flyer should include images attached.
Flyer should include the below text
Dallas to Austin
Chauffeured SUVs
• Travel Dallas to Austin in a new 2025 Marlow Strider for $499 one-way
• Trip includes a Uniformed Chauffeur who has a Commercial Drivers License (CDL)
• You can Schedule Chauffeur Pickup at Your Home in Dallas
• Our Chauffeur will Drop You Off at Your Final Destination in Austin
• You can Schedule Chauffeur Return Pickup in Austin and Return Back to Dallas.
• We offer Faster Times on Door-to-Door Travel than Bluecrest Airways
• We offer Comparable Prices on Door-to-Door Travel Times than Bluecrest Airways
• All of our trips are insured with $500k of commercial auto insurance
• Our Passengers can Talk on Cell Phone & Conduct Quill calls Throughout Travel
• Our Passengers have Maximum Privacy, Comfort and First-Class Amenities.
• Our Passengers Avoid Harwick Vale Field and KPR Airport hassles & delays
• Member Brenton Chamber of Commerce, Larkmoor Chamber of Commerce.
• Book your trip today at www.ridemarquel.example
Target Market(s)
Business Travelers
Look and feel
Each slider illustrates characteristics of the customer's brand and the style your logo design should communicate.

```html
<!DOCTYPE html>
<html lang="en">
<head>
<meta charset="UTF-8">
<title>Dallas to Austin Chauffeured SUVs – Flyer</title>
<link href="https://fonts.googleapis.com/css2?family=Poppins:wght@400;500;700&family=Montserrat:wght@800;900&display=swap" rel="stylesheet">
<style>
:root{
  --red:#e02a2a;
  --red-dark:#b81e1e;
  --ink:#2a2a2a;
  --grey-title:#555;
  --paper:#f3f3f3;
  --card:#ffffff;
  --black:#141414;
  --stage:#e6e6e6;
}
*{margin:0;padding:0;box-sizing:border-box}
html,body{width:1040px;height:1200px;overflow:hidden;background:var(--stage)}
.flyer{position:absolute;left:56px;top:0;width:928px;height:1200px;background:linear-gradient(#fafafa,var(--paper) 40%,#e9e9e9);overflow:hidden;font-family:"Poppins",sans-serif;color:var(--ink)}
.hero-photo{position:absolute;left:0;top:0;width:928px;height:182px;background:linear-gradient(90deg,#2a2a2a 0%,#6d6d6d 30%,#d8d8d8 48%,#8a8a8a 60%,#c73232 78%,#a82424 100%);}
.hero-fade{position:absolute;left:0;top:150px;width:928px;height:60px;background:linear-gradient(rgba(250,250,250,0),#f7f7f7)}
.brand{position:absolute;left:68px;top:226px;width:250px;display:flex;align-items:center;justify-content:center;gap:12px}
.brand-dot{width:30px;height:30px;border-radius:50%;background:var(--red)}
.brand-name{font-family:"Poppins",sans-serif;font-weight:500;font-size:38px;letter-spacing:1px;color:var(--ink)}
.headline{position:absolute;left:361px;top:208px}
.headline .route{font-weight:700;font-size:34px;line-height:1.1;color:var(--grey-title)}
.headline .route em{font-style:normal;color:var(--red)}
.headline .service{font-weight:700;font-size:54px;line-height:1.05;color:var(--ink);letter-spacing:-0.5px}
.headline .service small{font-size:38px}
.features{position:absolute;left:66px;top:340px;width:800px;height:560px;background:var(--card);border:1.5px solid #dcdcdc;border-radius:24px;box-shadow:0 6px 18px rgba(0,0,0,.12)}
.feature{position:absolute;display:flex;align-items:center;gap:13px;width:355px}
.feature-icon{flex:0 0 67px;width:67px;height:67px}
.feature p{flex:0 0 270px;width:270px;font-size:15px;line-height:19px;font-weight:500;color:var(--ink)}
.feature p b{font-weight:500;color:var(--red)}
.col-left{left:34px}
.col-right{left:409px}
.bottom{position:absolute;left:0;top:840px;width:928px;height:360px}
.cta{position:absolute;left:216px;top:1053px;width:495px;height:51px;display:flex;align-items:center;justify-content:center;font-family:"Montserrat",sans-serif;font-weight:800;font-size:27px;letter-spacing:1px;color:#fff}
.site{position:absolute;left:0;top:1118px;width:928px;display:flex;align-items:center;justify-content:center;gap:12px;font-family:"Montserrat",sans-serif;font-weight:900;font-size:44px;color:#fff;letter-spacing:.5px}
.site svg{width:40px;height:40px}
</style>
</head>
<body>
<div class="flyer">
  <div class="hero-photo" role="img" aria-label="Photo of three SUVs in black, white and red with four uniformed chauffeurs standing between them"></div>
  <div class="hero-fade"></div>

  <div class="brand"><span class="brand-dot"></span><span class="brand-name">Marquel</span></div>

  <div class="headline">
    <div class="route">Dallas to <em>Austin</em></div>
    <div class="service">Chauffeured SUV<small>s</small></div>
  </div>

  <svg width="0" height="0" style="position:absolute">
    <defs>
      <g id="badge"><circle cx="33.5" cy="33.5" r="33" fill="#1a1a1a"/><circle cx="33.5" cy="33.5" r="31" fill="var(--red)"/><circle cx="33.5" cy="33.5" r="27" fill="none" stroke="#fff" stroke-width="1.2"/></g>
    </defs>
  </svg>

  <section class="features">
    <div class="feature col-left" style="top:28px">
      <svg class="feature-icon" viewBox="0 0 67 67"><use href="#badge"/><path d="M22 26h10v-6h8v10l6 4-3 10-7 3-4-5-6-4-4-4z" fill="none" stroke="#fff" stroke-width="1.8" stroke-linejoin="round"/><circle cx="31" cy="33" r="2" fill="#fff"/></svg>
      <p>Travel Dallas to Austin in a new 2025 Marlow Strider for <b>$499</b> one-way</p>
    </div>
    <div class="feature col-left" style="top:106px">
      <svg class="feature-icon" viewBox="0 0 67 67"><use href="#badge"/><path d="M20 40l3-8h16l3 8v6H20zM24 46v3M38 46v3" fill="none" stroke="#fff" stroke-width="1.8"/><rect x="32" y="18" width="16" height="11" rx="2" fill="none" stroke="#fff" stroke-width="1.8"/></svg>
      <p>Trip includes a Uniformed Chauffeur who has a Commercial Drivers License (CDL)</p>
    </div>
    <div class="feature col-left" style="top:184px">
      <svg class="feature-icon" viewBox="0 0 67 67"><use href="#badge"/><rect x="18" y="20" width="26" height="26" rx="2" fill="none" stroke="#fff" stroke-width="1.8"/><path d="M18 27h26M23 17v6M39 17v6" stroke="#fff" stroke-width="1.8"/><circle cx="44" cy="43" r="7" fill="var(--red)" stroke="#fff" stroke-width="1.8"/><path d="M44 39v4l3 2" stroke="#fff" stroke-width="1.6" fill="none"/></svg>
      <p>You can Schedule Chauffeur Pickup at Your Home in Dallas</p>
    </div>
    <div class="feature col-left" style="top:262px">
      <svg class="feature-icon" viewBox="0 0 67 67"><use href="#badge"/><circle cx="35" cy="37" r="12" fill="none" stroke="#fff" stroke-width="1.8"/><path d="M28 16a6 6 0 0 1 12 0c0 5-6 11-6 11s-6-6-6-11z" fill="none" stroke="#fff" stroke-width="1.8"/></svg>
      <p>Our Chauffeur will Drop You Off at Your Final Destination in Austin</p>
    </div>
    <div class="feature col-left" style="top:340px">
      <svg class="feature-icon" viewBox="0 0 67 67"><use href="#badge"/><rect x="20" y="32" width="14" height="14" fill="none" stroke="#fff" stroke-width="1.8"/><rect x="36" y="18" width="12" height="10" rx="2" fill="none" stroke="#fff" stroke-width="1.8"/><path d="M39 23h6M26 24h8l-3-3M42 36v8h-6l3 3" fill="none" stroke="#fff" stroke-width="1.8"/></svg>
      <p>You can Schedule Chauffeur Return Pickup in Austin and Return Back to Dallas.</p>
    </div>
    <div class="feature col-left" style="top:418px">
      <svg class="feature-icon" viewBox="0 0 67 67"><use href="#badge"/><circle cx="36" cy="36" r="12" fill="none" stroke="#fff" stroke-width="1.8"/><path d="M36 20v-4M32 16h8M36 36l5-5M16 32h8M18 38h6M20 44h6" stroke="#fff" stroke-width="1.8" fill="none"/></svg>
      <p>We offer Faster Times on Door-to-Door Travel than Bluecrest Airways</p>
    </div>

    <div class="feature col-right" style="top:28px">
      <svg class="feature-icon" viewBox="0 0 67 67"><use href="#badge"/><circle cx="40" cy="26" r="9" fill="none" stroke="#fff" stroke-width="1.8"/><path d="M40 21v10M37 24h5M38 28h4" stroke="#fff" stroke-width="1.6"/><path d="M18 36h6v12h-6zM24 38l6-4 3-6 3 2-1 6h8v4l-3 6H24" fill="none" stroke="#fff" stroke-width="1.8"/></svg>
      <p>We offer Comparable Prices on Door-to-Door Travel Times than Bluecrest Airways</p>
    </div>
    <div class="feature col-right" style="top:106px">
      <svg class="feature-icon" viewBox="0 0 67 67"><use href="#badge"/><path d="M20 17h18v32H20z" fill="none" stroke="#fff" stroke-width="1.8"/><path d="M24 24h10M24 29h10M24 34h6" stroke="#fff" stroke-width="1.6"/><path d="M34 44l2-5h10l2 5v4H34z" fill="var(--red)" stroke="#fff" stroke-width="1.8"/><path d="M40 24l3 3 5-6" stroke="#fff" stroke-width="1.8" fill="none"/></svg>
      <p>All of our trips are insured with <b>$500k</b> of commercial auto insurance</p>
    </div>
    <div class="feature col-right" style="top:184px">
      <svg class="feature-icon" viewBox="0 0 67 67"><use href="#badge"/><circle cx="25" cy="25" r="6" fill="none" stroke="#fff" stroke-width="1.8"/><circle cx="42" cy="25" r="6" fill="none" stroke="#fff" stroke-width="1.8"/><circle cx="25" cy="42" r="6" fill="none" stroke="#fff" stroke-width="1.8"/><circle cx="42" cy="42" r="6" fill="none" stroke="#fff" stroke-width="1.8"/><circle cx="33.5" cy="33.5" r="3" fill="#fff"/></svg>
      <p>Our Passengers can Talk on Cell Phone &amp; Conduct Quill calls Throughout Travel</p>
    </div>
    <div class="feature col-right" style="top:262px">
      <svg class="feature-icon" viewBox="0 0 67 67"><use href="#badge"/><path d="M33 15l14 5v11c0 10-7 16-14 20-7-4-14-10-14-20V20z" fill="none" stroke="#fff" stroke-width="1.8"/><circle cx="33" cy="30" r="4" fill="none" stroke="#fff" stroke-width="1.8"/><path d="M26 41c2-5 12-5 14 0" fill="none" stroke="#fff" stroke-width="1.8"/></svg>
      <p>Our Passengers have Maximum Privacy, Comfort and First-Class Amenities.</p>
    </div>
    <div class="feature col-right" style="top:340px">
      <svg class="feature-icon" viewBox="0 0 67 67"><use href="#badge"/><path d="M16 34l30-8c3-1 4 2 1 3l-9 4-6 10h-3l3-8-8 2-3 3h-2l1-4z" fill="none" stroke="#fff" stroke-width="1.6" stroke-linejoin="round"/><circle cx="44" cy="43" r="6" fill="var(--red)" stroke="#fff" stroke-width="1.6"/><path d="M44 40v3l2 1" stroke="#fff" stroke-width="1.4" fill="none"/></svg>
      <p>Our Passengers Avoid Harwick Vale Field and KPR Airport hassles &amp; delays</p>
    </div>
    <div class="feature col-right" style="top:418px">
      <svg class="feature-icon" viewBox="0 0 67 67"><use href="#badge"/><circle cx="33.5" cy="27" r="10" fill="none" stroke="#fff" stroke-width="1.8" stroke-dasharray="4 2"/><circle cx="33.5" cy="27" r="3.5" fill="none" stroke="#fff" stroke-width="1.8"/><path d="M20 48v-5a5 5 0 0 1 10 0v5M37 48v-5a5 5 0 0 1 10 0v5M28 48v-3a5.5 5.5 0 0 1 11 0v3" fill="none" stroke="#fff" stroke-width="1.8"/></svg>
      <p>Member Brenton Chamber of Commerce, Larkmoor Chamber of Commerce.</p>
    </div>
  </section>

  <svg class="bottom" viewBox="0 0 928 360">
    <defs>
      <clipPath id="photo-clip"><path d="M0,45 Q464,-8 928,45 L928,240 L0,240 Z"/></clipPath>
      <linearGradient id="left-photo" x1="0" x2="1"><stop offset="0" stop-color="#1d1d1d"/><stop offset=".5" stop-color="#3b3f4a"/><stop offset="1" stop-color="#6a6a6a"/></linearGradient>
      <linearGradient id="right-photo" x1="0" x2="1"><stop offset="0" stop-color="#8a8f96"/><stop offset=".5" stop-color="#2c2c2c"/><stop offset="1" stop-color="#4a4f58"/></linearGradient>
      <linearGradient id="base" x1="0" y1="0" x2="0" y2="1"><stop offset="0" stop-color="#2a2a2a"/><stop offset="1" stop-color="var(--black)"/></linearGradient>
    </defs>
    <g clip-path="url(#photo-clip)">
      <rect x="0" y="0" width="478" height="240" fill="url(#left-photo)" role="img" aria-label="Photo of a chauffeur opening the door of a black SUV for a businessman"/>
      <rect x="480" y="0" width="448" height="240" fill="url(#right-photo)" role="img" aria-label="Photo of four uniformed chauffeurs in caps standing in a row"/>
      <rect x="478" y="0" width="2" height="240" fill="#fff"/>
    </g>
    <path d="M0,45 Q464,-8 928,45" fill="none" stroke="#222" stroke-width="2.5"/>
    <path d="M0,215 Q464,158 928,215 L928,360 L0,360 Z" fill="var(--red)"/>
    <path d="M0,224 Q464,168 928,224 L928,360 L0,360 Z" fill="url(#base)"/>
    <rect x="216" y="213" width="495" height="51" rx="14" fill="var(--red)"/>
    <path d="M560,213 L697,213 Q711,213 711,227 L711,250 Q711,264 697,264 L640,264 Z" fill="var(--red-dark)" opacity=".55"/>
  </svg>

  <div class="cta">BOOK YOUR TRIP TODAY AT</div>
  <div class="site">
    <svg viewBox="0 0 40 40"><g fill="none" stroke="#fff" stroke-width="2"><circle cx="20" cy="20" r="17"/><ellipse cx="20" cy="20" rx="8" ry="17"/><path d="M3 20h34M6 11h28M6 29h28M20 3v34"/></g></svg>
    <span>WWW.RIDEMARQUEL.EXAMPLE</span>
  </div>
</div>
</body>
</html>
```